KV Group

We need a new website for our company and since we had a very good work done for our logo in this site, we're back for the entire job.

Our company name is Marlowe Capital Group. We're adding files of examples of what we have done today. In my opinion we need a more attention lock in the site but yet financial simple work.

Our files (attached) will let you know what we have so far. We need a complete change but the colours should be the same, however you can change them not running away to far from the original, and of course matching with the logo.

We need examples for 3 kind of layouts.

- A HOME welcome layout
- An internal Layout with sidebar
- And internal Layout wide

We can buy image licenses if needed for assets.
Actually there are 5 slide images placed on the Welcome HOME, we need those there, but you can improve with better images to match the new website!!!

Target Market(s)

Clients looking for financial advisers, tax and funds specialist, currency advisers

Industry/Entity Type

Financial

Requirements
Must have
• all the fonts must be in accordance with the financial market sites........the welcome home page must be precise, neat and information accurate........the menu should be elegant........main focus on the Home page, should be also the PRIVATE ACCESS box log in.......

```html
<!DOCTYPE html>
<html lang="en">
<head>
<meta charset="utf-8">
<title>Marlowe Capital Group</title>
<link href="https://fonts.googleapis.com/css2?family=Montserrat:wght@400;600;700&family=Questrial&family=Arimo:wght@400;700&display=swap" rel="stylesheet">
<style>
:root{
  --orange:#f47920;
  --dark:#262626;
  --ink:#333;
  --grey:#8a8a8a;
  --line:#5a5a5a;
  --white:#fff;
  --navy:#1b2a5a;
  --green:#3a9a2a;
  --red:#d0141e;
  --badge-blue:#2c5aa8;
  --badge-green:#6ab04c;
  --badge-red:#a3192e;
}
*{box-sizing:border-box;margin:0;padding:0}
html,body{width:1016px;height:1200px;overflow:hidden;background:var(--white)}
body{position:relative;font-family:"Questrial",sans-serif;color:var(--ink)}
.abs{position:absolute}

/* header */
.brand{left:85px;top:44px;display:flex;align-items:center;gap:8px;font-family:"Montserrat",sans-serif;font-weight:600;font-size:15px;color:var(--dark)}
.brand-mark{width:18px;height:18px;background:var(--orange)}
.top-btn{top:17px;height:27px;display:flex;align-items:center;gap:5px;padding:0 5px;font-size:11.5px;color:var(--white);white-space:nowrap}
.top-btn.apply{left:735px;width:94px;background:var(--orange)}
.top-btn.contact{left:838px;width:94px;background:var(--dark)}
.main-nav{left:311px;top:60px;width:621px;height:31px;background:var(--dark);display:flex}
.main-nav a{color:var(--white);text-decoration:none;font-size:12px;display:flex;align-items:center;justify-content:center;padding:0 19px;white-space:nowrap}
.main-nav a.active{background:var(--orange);width:80px;padding:0}

/* hero */
.hero{left:85px;top:102px;width:847px;height:262px;background:linear-gradient(180deg,#0a0806 0%,#1b1410 55%,#3a2a18 82%,#181410 100%)}
.hero-title{left:99px;top:142px;font-family:"Montserrat",sans-serif;font-size:29px;font-weight:600;color:var(--orange);letter-spacing:1px;white-space:nowrap}
.hero-copy{left:99px;top:186px;font-size:12px;line-height:16px;color:var(--white)}
.hero-copy em{font-style:normal;color:var(--orange);font-size:13px}
.hero-btn{left:99px;top:226px;width:136px;height:34px;background:var(--orange);color:var(--white);font-family:"Montserrat",sans-serif;font-weight:600;font-size:14px;display:flex;align-items:center;justify-content:center}
.dots{left:99px;top:337px;display:flex;gap:5px}
.dots span{width:13px;height:13px;background:var(--white)}
.dots span:first-child{background:var(--orange)}

/* rates */
.rates{left:85px;top:364px;width:847px;height:43px;background:linear-gradient(180deg,#fafafa,#dedede)}
.rates-tag{left:85px;top:364px;width:114px;height:43px;background:var(--orange);clip-path:polygon(0 0,88% 0,100% 50%,88% 100%,0 100%);color:var(--white);font-family:"Arimo",sans-serif;font-weight:700;font-size:11px;display:flex;align-items:center;padding-left:13px}
.rate-list{left:196px;top:364px;height:43px;display:flex;align-items:center;font-family:"Arimo",sans-serif;font-size:10.5px;color:var(--navy);white-space:nowrap}
.rate-list span{padding:0 19px 0 0}
.rate-list i{font-style:normal;color:#aaa;padding-right:19px}
.rate-list b{font-weight:400;color:var(--green)}
.rate-list b.down{color:var(--red)}

/* welcome */
.welcome-title{left:85px;top:440px;font-family:"Montserrat",sans-serif;font-weight:600;font-size:29px;color:var(--orange);letter-spacing:.5px}
.welcome-text{left:85px;top:486px;width:545px;font-family:"Arimo",sans-serif;font-size:11px;line-height:17px;color:var(--grey)}
.welcome-btn{left:86px;top:619px;width:94px;height:28px;background:var(--orange);color:var(--white);font-size:11.5px;display:flex;align-items:center;justify-content:center}

/* privacy */
.privacy{left:677px;top:430px;width:255px;height:225px;background:var(--orange)}
.privacy h2{position:absolute;left:24px;top:22px;font-family:"Questrial",sans-serif;font-weight:400;font-size:15px;color:var(--white)}
.field{position:absolute;left:17px;width:220px;height:36px;background:var(--white);border:1px solid #e9c3a6;display:flex;align-items:center;gap:10px;padding-left:11px;color:var(--orange);font-size:12px}
.field.user{top:53px}
.field.pass{top:98px}
.sign-in{position:absolute;left:54px;top:147px;width:148px;height:35px;background:var(--dark);color:var(--white);font-family:"Montserrat",sans-serif;font-weight:600;font-size:14px;display:flex;align-items:center;justify-content:center}
.forgot{position:absolute;left:0;width:100%;top:193px;text-align:center;color:var(--white);font-size:12px}

/* services */
.card{top:684px;width:271px;height:174px;background:var(--dark);color:var(--white);text-align:center}
.card.orange{background:var(--orange)}
.card svg{position:absolute;left:50%;top:12px;transform:translateX(-50%)}
.card h3{position:absolute;left:0;right:0;top:83px;font-family:"Montserrat",sans-serif;font-weight:700;font-size:13.5px}
.card p{position:absolute;left:12px;right:12px;top:104px;font-size:11px;line-height:15px}

/* partners */
.verified{left:87px;top:903px;font-family:"Montserrat",sans-serif;font-weight:600;font-size:17.5px;color:var(--dark);letter-spacing:-.3px;white-space:nowrap}
.badge{top:896px}

/* footer */
.footer{left:85px;top:960px;width:847px;height:240px;background:var(--dark)}
.f-col{top:972px}
.f-col h4{font-family:"Montserrat",sans-serif;font-weight:600;font-size:12.5px;color:var(--orange);margin-bottom:6px;white-space:nowrap}
.f-col h4.sub{margin-top:14px;margin-bottom:2px}
.f-col a{display:block;width:107px;font-size:11px;color:#c9c9c9;text-decoration:none;height:22px;line-height:20px;border-bottom:1px dashed var(--line);white-space:nowrap}
.f-col a:last-child{border-bottom:0}
.copyright{left:130px;top:1166px;font-size:9.5px;color:#c9c9c9}
</style>
</head>
<body>

<header>
  <div class="abs brand"><span class="brand-mark"></span>Marlowe Capital Group</div>
  <div class="abs top-btn apply">
    <svg width="15" height="17" viewBox="0 0 16 18" fill="none" stroke="#fff" stroke-width="1.2"><rect x="1" y="1" width="12" height="16"/><path d="M5 12l7-8 2 2-7 8H5z"/></svg>
    Apply Now
  </div>
  <div class="abs top-btn contact">
    <svg width="17" height="14" viewBox="0 0 18 15" fill="#fff"><path d="M1 5c0-3 16-3 16 0v2h-4V5H5v2H1z"/><rect x="3" y="8" width="12" height="7" rx="1"/></svg>
    Contact Us
  </div>
  <nav class="abs main-nav">
    <a class="active">Home</a><a>About Us</a><a>Investments</a><a>Funds</a><a>Brokerage</a><a>Exchange</a><a>Accounts</a>
  </nav>
</header>

<section>
  <div class="abs hero" role="img" aria-label="Night skyline of a city business district with lit office towers"></div>
  <h1 class="abs hero-title">FINANCIAL MANAGEMENT</h1>
  <p class="abs hero-copy">We Offer tailored and flexible solutions for banking and<br>financial managment that <em>meets your business needs.</em></p>
  <div class="abs hero-btn">READ MORE</div>
  <div class="abs dots"><span></span><span></span><span></span><span></span><span></span></div>
</section>

<section>
  <div class="abs rates"></div>
  <div class="abs rate-list">
    <span>BP/UGX= <b class="down">4010.061274</b></span><i>|</i>
    <span>GBP/UAH= <b>12.65761</b></span><i>|</i>
    <span>GBP/UAH= <b>12.65761</b></span><i>|</i>
    <span>GBP/UAH= <b>12.65761</b></span><i>|</i>
    <span>GBP/UAH= <b>12.65761</b></span><i>|</i>
  </div>
  <div class="abs rates-tag">TODAY RATES</div>
</section>

<section>
  <h2 class="abs welcome-title">WELCOME</h2>
  <p class="abs welcome-text">Lorem ipsum dolor sit amet, consectetuer adipiscing elit, sed diam nonummy nibh euismod tincidunt ut laoreet dolore magna aliquam erat volutpat. Ut wisi enim ad minim veniam, quis nostrud exerci tation ullamcorper suscipit lobortis nisl ut aliquip ex ea commodo consequat. Duis autem vel eum iriure dolor in hendrerit in vulputate velit esse molestie consequat, vel illum dolore eu feugiat nulla facilisis at vero eros et accumsan et iusto odio dignissim qui blandit praesent luptatum zzril delenit augue duis dolore te feugait nulla facilisi. Nam liber tempor cum soluta nobis eleifend option congue nihil imperdiet doming id quod mazim placerat facer possim assum.</p>
  <div class="abs welcome-btn">READ MORE</div>

  <div class="abs privacy">
    <h2>PRIVACY ACCESS</h2>
    <div class="field user">
      <svg width="20" height="14" viewBox="0 0 20 14" fill="none" stroke="#f47920" stroke-width="1.5"><rect x="1" y="1" width="18" height="12" rx="1"/><path d="M1 1l9 7 9-7"/></svg>
      <b style="font-weight:700">Username</b>
    </div>
    <div class="field pass">
      <svg width="16" height="20" viewBox="0 0 16 20" fill="none" stroke="#f47920" stroke-width="1.5"><rect x="1" y="8" width="14" height="11" rx="1"/><path d="M4 8V5a4 4 0 018 0v3"/><path d="M8 12v3"/></svg>
      Password
    </div>
    <div class="sign-in">SIGN IN</div>
    <div class="forgot">Forgot Password?</div>
  </div>
</section>

<section>
  <div class="abs card" style="left:86px">
    <svg width="64" height="58" viewBox="0 0 64 58" fill="none" stroke="#fff" stroke-width="3"><rect x="2" y="2" width="60" height="42"/><path d="M26 44v6M38 44v6M16 54h32" stroke-width="4"/><path d="M22 16l10-5 10 5v12l-10 5-10-5z" fill="#fff"/></svg>
    <h3>MANAGEMENT AND STRAGEDY</h3>
    <p>Lorem ipsum dolor sit amet, consectet dipiscing elit, sed diam nonummy nibh euismod tincidunt ut laoreet dolore magna aliquam erat volutpat. Ut wisi enim ad minim veniam.</p>
  </div>
  <div class="abs card orange" style="left:374px">
    <svg width="66" height="62" viewBox="0 0 66 62" fill="none" stroke="#fff" stroke-width="3"><rect x="2" y="2" width="62" height="30"/><circle cx="33" cy="17" r="9" fill="#fff"/><circle cx="16" cy="42" r="8" fill="#fff"/><circle cx="40" cy="52" r="8" fill="#fff"/><circle cx="47" cy="32" r="7" fill="#fff"/></svg>
    <h3>FUNDS</h3>
    <p>Lorem ipsum dolor sit amet, consectet dipiscing elit, sed diam nonummy nibh euismod tincidunt ut laoreet dolore magna aliquam erat volutpat. Ut wisi enim ad minim veniam.</p>
  </div>
  <div class="abs card" style="left:662px">
    <svg width="66" height="62" viewBox="0 0 66 62"><circle cx="22" cy="22" r="18" fill="#fff"/><circle cx="44" cy="40" r="19" fill="#fff" stroke="#262626" stroke-width="3"/><path d="M22 10v24M44 28v24" stroke="#262626" stroke-width="3"/><path d="M40 4a20 20 0 0114 10M26 58a20 20 0 01-14-10" fill="none" stroke="#fff" stroke-width="3"/></svg>
    <h3>CURRENCY EXCHANGE</h3>
    <p>Lorem ipsum dolor sit amet, consectet dipiscing elit, sed diam nonummy nibh euismod tincidunt ut laoreet dolore magna aliquam erat volutpat. Ut wisi enim ad minim veniam.</p>
  </div>
</section>

<section>
  <h2 class="abs verified">VERIFIED AND PROTECTED BY:</h2>
  <svg class="abs badge" style="left:492px" width="82" height="34" viewBox="0 0 82 34" role="img" aria-label="Audit partner badge"><rect x="2" y="2" width="78" height="30" rx="3" fill="var(--badge-blue)"/></svg>
  <svg class="abs badge" style="left:608px" width="122" height="34" viewBox="0 0 122 34" role="img" aria-label="Privacy certification badge"><rect x="2" y="2" width="118" height="30" rx="3" fill="var(--badge-green)"/></svg>
  <svg class="abs badge" style="left:752px" width="38" height="38" viewBox="0 0 38 38" role="img" aria-label="Trust seal badge"><circle cx="19" cy="19" r="17" fill="var(--badge-blue)"/></svg>
  <svg class="abs badge" style="left:826px" width="92" height="34" viewBox="0 0 92 34" role="img" aria-label="Security verification badge"><rect x="2" y="2" width="88" height="30" rx="3" fill="var(--badge-red)"/></svg>
</section>

<footer>
  <div class="abs footer"></div>
  <div class="abs f-col" style="left:129px"><h4>ABOUT US</h4><a>Hisory</a><a>Expertize</a><a>Identity</a><a>Stragedy</a><a>Contact Us</a></div>
  <div class="abs f-col" style="left:270px"><h4>INVESTMENT</h4><a>Term Deposits</a><a>Managment</a><a>Client Relations</a><a>Financial Privacy</a><a>Tax Advice</a><a>Wealth Analysis</a><a>Private Equity</a></div>
  <div class="abs f-col" style="left:429px"><h4>FUNDS</h4><a>Overview</a><a>Administration</a><a>Funds Security</a><a>Core Services</a><a>Reporting</a><a>How it works?</a><a>Glossary</a></div>
  <div class="abs f-col" style="left:575px"><h4>CURRENCY EXCHANGE</h4><a style="margin-left:4px">Foreign Exchange</a><a style="margin-left:4px">Fx Forward</a><a style="margin-left:4px;border-bottom:0">Fx Options</a>
    <h4 class="sub" style="margin-left:4px">ACCOUNTS</h4><a style="margin-left:4px">Apply Now</a><a style="margin-left:4px">Private Access</a></div>
  <div class="abs f-col" style="left:771px"><h4>BROKERAGE</h4><a style="margin-left:5px">Institutional</a><a style="margin-left:5px">Research</a><a style="margin-left:5px">Trading</a></div>
  <p class="abs copyright">© Copyright 2013 MarloweCapital.com</p>
</footer>

</body>
</html>
```